Fishing Tackle Product Packaging Backdrop/Template

Hi Designers,
we require a versatile packaging backdrop/template design for our fishing tackle brand. The design will be used in printed packaging for a range of products from small to large so would need to be scaleable. It will most commonly be used on small printed card tags (2x3"), but we would like to be able to use it for other packaging aswell.
A section for our product details, which we can edit ourselves would be essential, this way we can use the template for any of our products. The back of the card will need a space for our barcodes.
The design needs to be predominantly macsuline and appeal to the modern carp angler. It also needs to pop so that our goods really stand out against our competitors. Please see our logo attached. It'd also be great to see our web address at the bottom, on both sides of the design: www.brelvanrigs.co.uk

Thanks in advance and good luck!
Brelvan Rigs Team
Updates

Target Market(s)

Male Carp Anglers (aprox ages 18-60)

Industry/Entity Type

Fishing Tackle

Requirements
Must have
• Our logo and web address, with a section for a barcode and product title/info

```html
<!DOCTYPE html>
<html lang="en">
<head>
<meta charset="utf-8">
<title>Brelvan Rigs – Fishing Tackle Tag Template</title>
<link href="https://fonts.googleapis.com/css2?family=Cabin:wght@500;700&display=swap" rel="stylesheet">
<style>
  :root {
    --paper: #ffffff;
    --lime: #8cc63f;
    --forest: #445b2a;
    --forest-deep: #2f3f1d;
    --barcode-zone: #dfe6d3;
    --outline: #111111;
  }
  html, body {
    margin: 0;
    padding: 0;
    width: 1200px;
    height: 1200px;
    overflow: hidden;
    background: var(--paper);
  }
  .canvas {
    position: relative;
    width: 1200px;
    height: 1200px;
    font-family: "Cabin", "Gill Sans", sans-serif;
  }
  .band {
    position: absolute;
    background: var(--lime);
  }
  .card-outline {
    position: absolute;
    border: 1.5px solid var(--outline);
    box-sizing: border-box;
    z-index: 2;
  }
  .brand-disc {
    position: absolute;
    width: 306px;
    height: 306px;
    border-radius: 50%;
    background: var(--paper);
    display: flex;
    align-items: center;
    justify-content: center;
    z-index: 3;
  }
  .brand-name {
    color: var(--forest);
    font-weight: 700;
    font-size: 44px;
    line-height: 1.05;
    text-align: center;
  }
  .front-band { left: 308px; top: 128px; width: 275px; height: 383px; }
  .front-card { left: 262px; top: 149px; width: 692px; height: 346px; }
  .front-disc { left: 292px; top: 165px; }

  .back-band { left: 462px; top: 636px; width: 280px; height: 391px; }
  .back-card { left: 262px; top: 660px; width: 692px; height: 346px; }
  .back-disc { left: 448px; top: 680px; }

  .product-copy {
    position: absolute;
    left: 612px;
    top: 182px;
    width: 300px;
    text-align: center;
    color: var(--forest);
    z-index: 3;
  }
  .category {
    display: flex;
    align-items: center;
    justify-content: center;
    gap: 14px;
    font-weight: 500;
    font-size: 40px;
    letter-spacing: 5px;
    color: var(--forest-deep);
    line-height: 1;
  }
  .category .rule {
    width: 38px;
    height: 3px;
    background: var(--forest-deep);
  }
  .product-title {
    margin-top: 4px;
    font-weight: 700;
    font-size: 80px;
    letter-spacing: 1px;
    line-height: 1;
  }
  .barcode-zone {
    position: absolute;
    left: 637px;
    top: 338px;
    width: 260px;
    height: 74px;
    background: var(--barcode-zone);
    z-index: 3;
  }
  .web-address {
    position: absolute;
    left: 612px;
    top: 436px;
    width: 310px;
    text-align: center;
    font-weight: 700;
    font-size: 35px;
    line-height: 1;
    color: var(--forest);
    letter-spacing: 0.5px;
    z-index: 3;
  }
</style>
</head>
<body>
  <main class="canvas">
    <section class="tag tag-front" aria-label="Tag front">
      <div class="band front-band"></div>
      <div class="card-outline front-card"></div>
      <div class="brand-disc front-disc">
        <span class="brand-name">Brelvan<br>Rigs</span>
      </div>
      <div class="product-copy">
        <div class="category"><span class="rule"></span>FISHING<span class="rule"></span></div>
        <div class="product-title">TACKLE</div>
      </div>
      <div class="barcode-zone" role="img" aria-label="Space reserved for the product barcode"></div>
      <div class="web-address">brelvanrigs.co.uk</div>
    </section>

    <section class="tag tag-back" aria-label="Tag back">
      <div class="band back-band"></div>
      <div class="card-outline back-card"></div>
      <div class="brand-disc back-disc">
        <span class="brand-name">Brelvan<br>Rigs</span>
      </div>
    </section>
  </main>
</body>
</html>
```